依頼詳細
レスポンシブウェブデザインを意識したデザインでお願いします。

デザインに関しては、添付してあるデザインレイアウトシートを基にお願いします。
参考サイトのURLはデザインレイアウトシートに記載してあります。
色合いはグリーンかブルーを基調にお願いします。
新規のウェブサイトですので、既存サイトはありません。
ロゴも不要です。(後ではめ込むので社名だけテキストでレイアウトをお願いします。)
また、写真データも添付するので、レイアウトシートのイメージ画像に当て込んでください。

まずはパソコンサイトのデザインをお願いします。
当選後、スマホデザインをお願いします。

既存のテンプレートを使う場合は
テンプレート名を下記のような記載を提案の中にいれてください。
例:WordpressテーマはCorpLumen、デザインスキンは無料のQRN2019 LX4(http://corplumen.example/ex_plugin/qrnfuji2019_lx4/)をベースにデザインいたしました。
など

写真データで足りない場合は、一旦他のサイトや参考URLの写真をサンプルとして入れてください。(サンプルなどの表記をお願いします)
また、購入が必要な写真などを利用した場合は、Pixora Stock(https://stock.pixora-img.example/jp/)からファイル番号と価格を教えてください。
ページ数
1ページ
希望イメージ
シンプル 複雑
単色 カラフル
暗い 明るい
日常 高級
遊び心 厳粛
未来的 伝統的
女性的 男性的
希望する色
青系、緑系
納品ファイル
• イラストレーター形式 (.ai)
• フォトショップ形式 (.psd)
• PNG形式 (.png)
補足説明
上記のいずれか1つ。アウトラインありとなしの2つ。

こちらの要望を汲んで、デザインしていただきました。
ありがとうございました。

たくさんのご提案ありがとうございました。
次回もぜひ、よろしくお願い致します。

```html
<!DOCTYPE html>
<html lang="ja">
<head>
<meta charset="utf-8">
<title>有限会社 翠栄</title>
<link href="https://fonts.googleapis.com/css2?family=Noto+Sans+JP:wght@400;500;700&family=Noto+Serif+JP:wght@400;500&family=Roboto:wght@500;700;900&display=swap" rel="stylesheet">
<style>
:root{
  --green:#2f9a63;
  --green-pale:#d5edd6;
  --ink:#222;
  --text:#555;
  --dark:#333;
  --white:#fff;
}
*{box-sizing:border-box;margin:0;padding:0}
html,body{width:1200px;height:3655px;overflow:hidden}
body{position:relative;font-family:"Noto Sans JP",sans-serif;color:var(--ink);background:var(--white)}
.abs{position:absolute}
.ph{position:absolute}
.site-header{position:absolute;left:0;top:0;width:1200px;height:57px;background:var(--white);z-index:5}
.brand{position:absolute;left:40px;top:18px;display:flex;align-items:center;gap:8px;font-weight:700;font-size:19px;color:var(--ink)}
.brand-mark{width:18px;height:18px;background:var(--green)}
.brand small{font-size:15px;margin-right:4px}
.gnav{position:absolute;right:260px;top:22px;display:flex;gap:46px;font-size:14px;font-weight:500}
.header-cta{position:absolute;right:0;top:0;width:152px;height:57px;background:var(--green);color:#fff;font-size:15px;font-weight:700;display:flex;align-items:center;justify-content:center}
.hero{left:0;top:57px;width:1200px;height:621px;background:linear-gradient(180deg,#e6e9ea 0%,#cfd8d8 45%,#d3d5d3 75%,#c9cac8 100%)}
.hero-copy{position:absolute;left:567px;top:116px;width:64px;height:370px;background:#fff;writing-mode:vertical-rl;font-family:"Noto Serif JP",serif;font-size:35px;letter-spacing:6px;display:flex;align-items:center;justify-content:center;color:#222}
.sec-title{position:absolute;font-size:28px;font-weight:500;letter-spacing:1px}
.sec-en{position:absolute;font-family:"Roboto",sans-serif;font-weight:700;font-size:16px;letter-spacing:2px;color:var(--green)}
.sec-bar{position:absolute;width:32px;height:2px;background:#222}
.body-text{position:absolute;font-size:12px;line-height:21px;color:var(--text);letter-spacing:.5px}
.big-en{position:absolute;font-family:"Roboto",sans-serif;font-weight:700;color:var(--green);text-align:right;line-height:1;letter-spacing:-1px}
.deco-kanji{position:absolute;writing-mode:vertical-rl;font-family:"Noto Serif JP",serif;color:rgba(120,120,120,.22);font-size:72px;line-height:1.1}
.biz-bg{left:120px;top:1534px;width:1080px;height:639px;background:var(--green-pale)}
.card{position:absolute;width:257px;height:274px;background:#fff}
.card-img{height:145px;background:linear-gradient(160deg,#e8eceb,#b8c0bf)}
.card h3{text-align:center;font-size:16px;font-weight:700;margin-top:14px}
.card p{font-size:11.5px;line-height:20px;color:var(--text);padding:6px 22px 0;letter-spacing:.5px}
.card-arrow{position:absolute;right:0;bottom:0;width:20px;height:20px;background:var(--green);color:#fff;font-size:10px;display:flex;align-items:center;justify-content:center}
.btn-green{position:absolute;width:201px;height:30px;background:var(--green);color:#fff;font-size:12px;display:flex;align-items:center;padding:0 16px;justify-content:space-between}
.info-bg{left:0;top:2663px;width:681px;height:315px;background:var(--green-pale)}
.news{position:absolute;left:440px;top:2741px;width:560px;background:#fff;border-top:2px solid var(--green)}
.news li{list-style:none;height:48px;display:flex;align-items:center;font-size:12px;border-bottom:1px solid #ddd;padding-left:22px}
.news .date{font-family:"Roboto",sans-serif;font-weight:500;width:100px}
.news .tag{width:80px;height:22px;background:var(--green-pale);font-size:11px;font-weight:700;display:flex;align-items:center;justify-content:center;margin-right:24px}
.contact{left:0;top:3077px;width:1200px;height:319px;background:linear-gradient(180deg,#3aa468,#2f9a63)}
.contact-lead{position:absolute;left:0;width:1200px;top:61px;text-align:center;color:#fff;font-size:16px;font-weight:700;letter-spacing:2px}
.contact-btn{position:absolute;left:416px;top:118px;width:368px;height:62px;background:#333;color:#fff;font-weight:700;font-size:18px;display:flex;align-items:center;justify-content:center;letter-spacing:1px}
.contact-btn span{position:absolute;right:24px}
.tel{position:absolute;left:0;width:1200px;top:196px;text-align:center;color:#fff;font-family:"Roboto",sans-serif;font-weight:700;font-size:33px;letter-spacing:1px;display:flex;justify-content:center;align-items:center;gap:6px}
.tel-hours{position:absolute;left:0;width:1200px;top:240px;text-align:center;color:#fff;font-size:11px}
.site-footer{left:0;top:3396px;width:1200px;height:213px;background:var(--dark);color:#fff}
.site-footer .brand{left:208px;top:76px;color:#fff}
.f-addr{position:absolute;left:208px;top:112px;font-size:11px}
.f-tel{position:absolute;left:208px;top:136px;font-size:15px;letter-spacing:1px}
.f-nav{position:absolute;right:207px;top:82px;font-size:11px;display:flex}
.f-nav span{padding:0 18px;border-left:1px solid #888}
.f-nav span:first-child{border-left:none}
.f-nav span:last-child{padding-right:0}
.f-sub{top:134px}
.copy{left:0;top:3609px;width:1200px;height:46px;background:#fff;text-align:center;font-size:10px;line-height:46px;color:#444}
</style>
</head>
<body>

<header class="site-header">
  <div class="brand"><span class="brand-mark"></span><span><small>有限会社</small>翠栄</span></div>
  <nav class="gnav"><span>ホーム</span><span>お知らせ</span><span>会社紹介</span><span>業務内容</span><span>採用情報</span></nav>
  <div class="header-cta">お問い合わせ</div>
</header>

<section class="abs hero" role="img" aria-label="資材置き場に積み上げられた足場資材の写真">
  <div class="hero-copy">縁の下の力持ち。</div>
</section>

<div class="ph" style="left:0;top:752px;width:600px;height:404px;background:linear-gradient(90deg,#f2f3f3 0%,#d5d9d8 40%,#eceeed 100%)" role="img" aria-label="倉庫前に並ぶ資材の写真"></div>
<div class="ph" style="left:440px;top:850px;width:480px;height:272px;background:linear-gradient(180deg,#eef0ef,#bfc3bf 70%,#e0e2df)" role="img" aria-label="積み重ねられたパイプ資材の写真"></div>
<div class="abs" style="left:186px;top:760px;width:384px;height:230px;background:#fff"></div>
<div class="deco-kanji" style="left:870px;top:770px">資材</div>
<h2 class="sec-title" style="left:199px;top:770px">当社の特徴</h2>
<div class="sec-en" style="left:199px;top:814px">ABOUT</div>
<div class="sec-bar" style="left:199px;top:855px"></div>
<p class="body-text" style="left:199px;top:882px;width:362px">当社の特徴内容が入ります。ダミーテキスト。当社の特徴内容が入ります。ダミーテキスト。当社の特徴内容が入ります。ダミーテキスト。当社の特徴内容が入ります。ダミーテキスト。当社の特徴内容が入ります。ダミーテキスト。</p>
<div class="big-en" style="right:200px;top:1062px;font-size:70px">THOUSANDS OF<br>MATERIALS</div>

<h2 class="sec-title" style="left:199px;top:1266px">業務内容</h2>
<div class="sec-en" style="left:199px;top:1310px">BUSINESS CONTENTS</div>
<div class="sec-bar" style="left:199px;top:1352px"></div>
<p class="body-text" style="left:199px;top:1378px;width:802px">業務内容テキストが入ります。ダミーテキスト。業務内容テキストが入ります。ダミーテキスト。業務内容テキストが入ります。ダミーテキスト。業務内容テキストが入ります。ダミーテキスト。業務内容テキストが入ります。ダミーテキスト。</p>
<div class="abs biz-bg"></div>

<article class="card" style="left:199px;top:1453px"><div class="card-img" role="img" aria-label="積まれた足場板の写真"></div><h3>タイトル</h3><p>テキストテキストテキストテキストテキストテキストテキストテキストテキストテキストテキスト</p><span class="card-arrow">›</span></article>
<article class="card" style="left:471px;top:1453px"><div class="card-img" role="img" aria-label="ラックに並ぶパイプの写真"></div><h3>タイトル</h3><p>テキストテキストテキストテキストテキストテキストテキストテキストテキストテキストテキスト</p><span class="card-arrow">›</span></article>
<article class="card" style="left:743px;top:1453px"><div class="card-img" role="img" aria-label="穴あき鋼板の写真"></div><h3>タイトル</h3><p>テキストテキストテキストテキストテキストテキストテキストテキストテキストテキストテキスト</p><span class="card-arrow">›</span></article>
<article class="card" style="left:199px;top:1766px"><div class="card-img" role="img" aria-label="並べられた金属部材の写真"></div><h3>タイトル</h3><p>テキストテキストテキストテキストテキストテキストテキストテキストテキストテキストテキスト</p><span class="card-arrow">›</span></article>
<article class="card" style="left:471px;top:1766px"><div class="card-img" role="img" aria-label="赤と銀のパイプ資材の写真"></div><h3>タイトル</h3><p>テキストテキストテキストテキストテキストテキストテキストテキストテキストテキストテキスト</p><span class="card-arrow">›</span></article>
<article class="card" style="left:743px;top:1766px"><div class="card-img" role="img" aria-label="作業場で資材を扱う作業員の写真"></div><h3>タイトル</h3><p>テキストテキストテキストテキストテキストテキストテキストテキストテキストテキストテキスト</p><span class="card-arrow">›</span></article>

<div class="deco-kanji" style="left:510px;top:2268px;font-size:80px">挑戦</div>
<div class="ph" style="left:600px;top:2134px;width:400px;height:419px;background:linear-gradient(135deg,#a9b7b4,#6f7f7c 50%,#c3cbc9)" role="img" aria-label="作業する職人たちの写真"></div>
<h2 class="sec-title" style="left:199px;top:2283px">採用情報</h2>
<div class="sec-en" style="left:199px;top:2327px">RECRUITMENT</div>
<div class="sec-bar" style="left:199px;top:2368px"></div>
<p class="body-text" style="left:199px;top:2394px;width:300px">採用情報テキストが入ります。ダミーテキスト。採用情報テキストが入ります。<br>テキスト。採用情報テキストが入ります。ダミーテキスト。採用情報テキストが入ります。</p>
<div class="btn-green" style="left:199px;top:2503px"><span>採用情報はこちら</span><span>›</span></div>
<div class="big-en" style="right:200px;top:2496px;font-size:68px">CHALLENGE</div>

<div class="abs info-bg"></div>
<h2 class="sec-title" style="left:199px;top:2738px">お知らせ</h2>
<div class="sec-en" style="left:199px;top:2782px">INFORMATION</div>
<div class="sec-bar" style="left:199px;top:2823px"></div>
<div class="btn-green" style="left:199px;top:2855px"><span>お知らせ一覧</span><span>›</span></div>
<ul class="news">
  <li><span class="date">2020.00.00</span><span class="tag">お知らせ</span><span>○○○○○の対応について</span></li>
  <li><span class="date">2020.00.00</span><span class="tag">お知らせ</span><span>○○○○○○○○○○を更新しました</span></li>
  <li><span class="date">2020.00.00</span><span class="tag">お知らせ</span><span>ホームページリニューアルのお知らせ</span></li>
</ul>

<section class="abs contact" role="img" aria-label="緑色に重ねた資材かごの写真背景">
  <p class="contact-lead">ご質問などお気軽にお問い合わせください</p>
  <div class="contact-btn">お問い合わせはこちら<span>›</span></div>
  <div class="tel"><svg width="26" height="26" viewBox="0 0 24 24"><path fill="#fff" d="M6.6 10.8a15.1 15.1 0 0 0 6.6 6.6l2.2-2.2a1 1 0 0 1 1-.25 11.4 11.4 0 0 0 3.6.57 1 1 0 0 1 1 1V20a1 1 0 0 1-1 1A17 17 0 0 1 3 4a1 1 0 0 1 1-1h3.5a1 1 0 0 1 1 1c0 1.25.2 2.450.57 3.57a1 1 0 0 1-.25 1z"/></svg>000-123-4567</div>
  <p class="tel-hours">受付時間 00:00〜00:00</p>
</section>

<footer class="abs site-footer">
  <div class="brand"><span class="brand-mark"></span><span><small>有限会社</small>翠栄</span></div>
  <p class="f-addr">〒000-0000 新潟県 架空市緑町1番2号</p>
  <p class="f-tel">TEL 000-123-4567</p>
  <nav class="f-nav"><span>ホーム</span><span>お知らせ</span><span>会社紹介</span><span>業務内容</span><span>採用情報</span><span>お問い合わせ</span></nav>
  <nav class="f-nav f-sub"><span>個人情報保護法</span><span>サイトポリシー</span></nav>
</footer>
<div class="abs copy">Copyright © SUIEI. All Rights Reserved.</div>

</body>
</html>
```